New Business Card for Odd Bit Designs

I create and make jewellery and Clothing. But when it comes to business card design I fail completely.

Sketching is my area, drawing, putting things together neatly, not so much.

Here is a little blurb about my company:

Odd Bit Designs is a truly unique customer experience. Work one on one with Owner Marla Pemberton to make your costuming dreams come true.

Not after a costume? Browse through the store for a look at beautiful and unique piece of jewellery. Each piece has been put together by Marla, by hand. You'll find Steampunk, gothic, lolita and other quirky styles.

Want something else? What abotu a pair of warm kitty paws? A Pair of Kitty ears? A pony tail to wear on your jeans? There are so many options and things to choose! You will want to take it all home.

I have attached the previous business card with my mascot "Greta" As you can see there is a very Greta of Cloudmere feel to the overall company, with references to The Lost Tinker, and the idea that "We are all made here".

Colour's to use would be purple and blue. The winning design would show the unique but professional approach that Odd Bit Designs takes when creating each piece for their customers.

Reason: Wanted to give you a chance to go over feed back that has been sent out. I am committed to paying for the design that I will use. I think another week will help tweak things up.

Nerds, Geeks and Sci-Fi people aged 20 - 34 both Male and Female

Store

• Website address: www.oddbitdesigns.net

Yeah, rest is up too you!
• Honestly, if you could make the whole thing look like a Hugh Pellbrook "Greta of Cloudmere" Drawing with the same line working style that would be amazing!

But I won't restrict you! I'd like to see what you can come up with.

```html
<!DOCTYPE html>
<html lang="en">
<head>
<meta charset="utf-8">
<title>Odd Bit Designs – Business Card</title>
<link rel="stylesheet" href="https://fonts.googleapis.com/css2?family=Lobster&family=Noto+Serif:wght@700&display=swap">
<style>
  :root {
    --paper: #ffffff;
    --teal: #00a9bb;
    --teal-soft: #4fb9c6;
    --mist: #c3d8dc;
    --fog: #dadde2;
    --lilac: #bb9cc2;
    --plum: #8c3d93;
    --plum-back: #8e3f92;
    --ink-brown: #704d18;
    --orange: #f3921f;
    --gold: #eab54a;
  }
  * { margin: 0; padding: 0; box-sizing: border-box; }
  html, body {
    width: 1200px;
    height: 1032px;
    overflow: hidden;
    background: var(--paper);
  }
  .canvas {
    position: relative;
    width: 1200px;
    height: 1032px;
  }
  .card {
    position: absolute;
    width: 464px;
    height: 802px;
  }
  .card--front {
    left: 113px;
    top: 113px;
    background: linear-gradient(to bottom,
      #07a3b2 0%,
      var(--teal-soft) 25%,
      #96c8d0 40%,
      var(--mist) 50%,
      var(--fog) 62%,
      #d6cdd8 72%,
      var(--lilac) 84%,
      var(--plum) 100%);
  }
  .card__column {
    position: absolute;
    left: 60px;
    top: 0;
    width: 344px;
    height: 450px;
    background: linear-gradient(to bottom,
      rgba(0, 180, 196, 0.55) 0%,
      rgba(0, 180, 196, 0.35) 30%,
      rgba(200, 220, 224, 0.2) 75%,
      rgba(218, 221, 226, 0) 100%);
  }
  .contact {
    position: absolute;
    left: 0;
    top: 196px;
    width: 100%;
    text-align: center;
  }
  .contact__name {
    font-family: "Lobster", cursive;
    font-weight: 400;
    font-size: 40px;
    line-height: 56px;
    color: var(--ink-brown);
    letter-spacing: 0.5px;
  }
  .contact__rule {
    width: 308px;
    height: 1px;
    margin: 4px auto 14px;
    background: var(--ink-brown);
  }
  .contact__email {
    font-family: "Noto Serif", serif;
    font-weight: 700;
    font-size: 22px;
    line-height: 30px;
    color: var(--ink-brown);
  }
  .contact__web {
    font-family: "Lobster", cursive;
    font-size: 26px;
    line-height: 40px;
    color: var(--orange);
  }
  .card--back {
    left: 622px;
    top: 115px;
    background: var(--plum-back);
    display: flex;
    align-items: center;
    justify-content: center;
  }
  .tagline {
    font-family: "Lobster", cursive;
    font-weight: 400;
    font-size: 50px;
    line-height: 58px;
    color: var(--gold);
    text-align: center;
    margin-top: -20px;
  }
</style>
</head>
<body>
  <main class="canvas">
    <section class="card card--front">
      <div class="card__column"></div>
      <div class="contact">
        <h1 class="contact__name">Marla Pemberton</h1>
        <div class="contact__rule"></div>
        <p class="contact__email">odd.bit.design@postbox.net</p>
        <p class="contact__web">www.oddbitdesigns.net</p>
      </div>
    </section>
    <section class="card card--back">
      <p class="tagline">Handcrafted<br>flighs of fancy</p>
    </section>
  </main>
</body>
</html>
```